***PLASTIC*** Business Card Design

1 sided business card design
The card will be screen printed on plastic, so colour and fonts must be strong.

Must use the colours in the logo eps attached (Black/Ivory/White). Other colour(s) can be added.

Four (4) examples of how the logo can be printed are included in the logo eps attached.

The business card should highlight the logo. The card will be given to architects, interior designers and builders. It should look sophisticated but also innovative.

Do not cover the whole card with colour as it is important than some of the frosted plastic card is visible.

Be creative.

Target Market(s)

architects, interior designers and builders and wealthy home owners

Industry/Entity Type

Plastic

Requirements
Must have
• Must use the colours in the logo eps attached (Black/Ivory/White). Other colour(s) can be added if necessary.

The font is Square721 ExBT but has been a little thickened. It is not essential that you use this font. The name should be a stronger version of the font than other details.

The card will be printed on PVC - see http://www.voltrap.com.au/pricelistbcardsplastic.php

Final artwork must be print ready. You must use the printing spec at http://www.voltrap.com.au/2011%20PVC-TW.pdf

The actual details to be typeset ono the card are:

Dorian Welch

Mobile: 0412 806133
email: info@halcoworks.com.au
www.halcoworks.com.au

PO Box 53, Altona, Vic 3018

Plastering | Rendering | Cornicing

```html
<!DOCTYPE html>
<html lang="en">
<head>
<meta charset="utf-8">
<title>Halco Plastering – Business Card</title>
<link href="https://fonts.googleapis.com/css2?family=Poppins:wght@400;600&display=swap" rel="stylesheet">
<style>
  :root {
    --page-bg: #d9dde3;
    --frost-light: #eef3f8;
    --frost-mid: #d3dde8;
    --frost-edge: #8d9db2;
    --panel-black: #231f20;
    --panel-rim: #6b6d70;
    --icon-grey: #bbbbbb;
    --white: #ffffff;
  }
  * { margin: 0; padding: 0; box-sizing: border-box; }
  html, body {
    width: 1200px; height: 900px; overflow: hidden;
    background: var(--page-bg);
    font-family: "Poppins", sans-serif;
  }
  .card {
    position: absolute; left: 100px; top: 135px;
    width: 1000px; height: 630px;
    border-radius: 36px;
    border: 2px solid var(--frost-edge);
    background: radial-gradient(ellipse at 68% 42%, var(--frost-light) 0%, var(--frost-mid) 75%);
    overflow: hidden;
  }
  .card__panel { position: absolute; left: 0; top: 0; }
  .contact {
    position: absolute; left: 66px; top: 0;
    color: var(--white);
  }
  .contact__name {
    position: absolute; top: 196px; white-space: nowrap;
    font-size: 39px; font-weight: 600; letter-spacing: -0.5px;
  }
  .contact__list {
    position: absolute; top: 280px; list-style: none;
    font-size: 23px; font-weight: 400; line-height: 33px;
  }
  .contact__list li { display: flex; align-items: center; white-space: nowrap; }
  .contact__icon { width: 22px; height: 22px; margin-right: 18px; flex: none; }
  .contact__address {
    position: absolute; top: 396px; white-space: nowrap;
    font-size: 23px;
  }
  .contact__services {
    position: absolute; top: 497px; left: 2px; white-space: nowrap;
    font-size: 23px;
  }
  .brand {
    position: absolute; left: 515px; top: 240px; width: 470px;
    text-align: center; color: var(--panel-black);
    font-weight: 600;
  }
  .brand__name { font-size: 96px; line-height: 1; letter-spacing: 20px; padding-left: 20px; }
  .brand__trade { font-size: 35px; letter-spacing: 21px; margin-top: 12px; padding-left: 21px; }
</style>
</head>
<body>
  <div class="card">
    <svg class="card__panel" width="1000" height="630" viewBox="0 0 1000 630" aria-hidden="true">
      <path d="M27 24 H490 V204 L458 222 L490 240 V602 H62 Q27 602 27 567 Z"
            fill="var(--panel-black)" stroke="var(--panel-rim)" stroke-width="6"/>
      <path d="M490 21 V204 L458 222 L490 240 V605" fill="none" stroke="var(--frost-mid)" stroke-width="4"/>
    </svg>

    <div class="contact">
      <h1 class="contact__name">Dorian Welch</h1>
      <ul class="contact__list">
        <li>
          <svg class="contact__icon" viewBox="0 0 22 22" aria-hidden="true">
            <rect x="6" y="3" width="10" height="17" rx="1.5" fill="none" stroke="var(--icon-grey)" stroke-width="1.6"/>
            <rect x="8" y="6" width="6" height="5" fill="var(--icon-grey)"/>
          </svg>0412 806133
        </li>
        <li>
          <svg class="contact__icon" viewBox="0 0 22 22" aria-hidden="true">
            <rect x="2" y="5" width="18" height="12" fill="none" stroke="var(--icon-grey)" stroke-width="1.6"/>
            <path d="M2 5 L11 12 L20 5 M2 17 L9 11 M20 17 L13 11" fill="none" stroke="var(--icon-grey)" stroke-width="1.4"/>
          </svg>info@halcoworks.com.au
        </li>
        <li>
          <svg class="contact__icon" viewBox="0 0 22 22" aria-hidden="true">
            <circle cx="11" cy="11" r="8.5" fill="none" stroke="var(--icon-grey)" stroke-width="1.5"/>
            <ellipse cx="11" cy="11" rx="3.8" ry="8.5" fill="none" stroke="var(--icon-grey)" stroke-width="1.3"/>
            <path d="M2.5 11 H19.5 M4 7 H18 M4 15 H18" stroke="var(--icon-grey)" stroke-width="1.2"/>
          </svg>www.halcoworks.com.au
        </li>
      </ul>
      <p class="contact__address">PO Box 53, Elmvale, Vic 3099</p>
      <p class="contact__services">Plastering | Rendering | Cornicing</p>
    </div>

    <div class="brand">
      <div class="brand__name">HALCO</div>
      <div class="brand__trade">PLASTERING</div>
    </div>
  </div>
</body>
</html>
```